Email banner for a marketing campaign

Hi there,

We are running every 2x months a marketing campaign which is touching on some of our key service offering. The next campaign is starting in June and will be focusing on a service called "Managed Backup & Disaster Recovery (DR)". You can read more about this service by visiting https://bluecrest-it.co.uk/solutions/business-continuity-disaster-recovery/.

Below the wording that needs to figure on the banner, please ask if any of this wouldn't be clear.

Heading: Ransomware hits a business every 11 seconds
2nd Heading: Why take the risk of not being able to recover, let our Backup & DR experts manage this for you
<Green tick>: Regular Backup & DR Tests
<Green tick>: Quick Recovery Times
<Green tick>: 24/7 Support
Fennick Logo: Bottom right corner

Here the dimensions for the banner (480 x 152).

Thanks,

```html
<!DOCTYPE html>
<html lang="en">
<head>
<meta charset="utf-8">
<title>Managed Backup &amp; DR – Email Banner</title>
<link href="https://fonts.googleapis.com/css2?family=Anton&family=Fira+Sans:wght@600;700&family=Merienda:wght@700&display=swap" rel="stylesheet">
<style>
  :root {
    --panel-light: #eceef1;
    --panel-mid: #d9dce2;
    --stripe: #ffffff;
    --tech-deep: #0b1a4a;
    --tech-blue: #1f4fb8;
    --tech-violet: #5a2a8c;
    --tech-red: #b8324a;
    --box-pink: #c98a95;
    --tick-green: #1f6b2a;
    --label-dark: #1d1d24;
    --heading-white: #ffffff;
    --alert-red: #ef3b3b;
    --sub-pink: #fde3ec;
    --brand-red: #e2463f;
    --band-dark: #2a0c3a;
    --band-violet: #7a1d8f;
    --ink: #000000;
  }
  * { margin: 0; padding: 0; box-sizing: border-box; }
  html, body { width: 1200px; height: 937px; overflow: hidden; background: #ffffff; }
  .sheet { position: relative; width: 1200px; height: 937px; overflow: hidden; }

  .banner { position: absolute; left: 0; width: 1200px; overflow: hidden; }
  .banner--top { top: 0; height: 393px; }
  .banner--bottom { top: 511px; height: 426px; }

  .tech-backdrop {
    position: absolute; inset: 0;
    background:
      radial-gradient(ellipse at 70% 60%, rgba(184,50,74,.55), transparent 55%),
      radial-gradient(ellipse at 90% 20%, rgba(90,42,140,.7), transparent 60%),
      linear-gradient(135deg, var(--tech-blue), var(--tech-deep) 55%, var(--tech-violet));
  }
  .light-panel {
    position: absolute; inset: 0;
    background: linear-gradient(180deg, var(--panel-light), var(--panel-mid));
    clip-path: polygon(0 0, 440px 0, 600px 100%, 0 100%);
  }
  .diagonal-stripe {
    position: absolute; inset: 0;
    background: var(--stripe);
    clip-path: polygon(440px 0, 480px 0, 640px 100%, 600px 100%);
    opacity: .85;
  }

  .banner-content { position: absolute; left: 0; bottom: 0; width: 1200px; height: 393px; }

  .tick-box {
    position: absolute; width: 69px; height: 69px;
    background: var(--box-pink); border: 3px solid #ffffff;
  }
  .tick-box svg { width: 100%; height: 100%; display: block; }
  .tick-box--tests { left: 64px; top: 27px; }
  .tick-box--recovery { left: 64px; top: 229px; }
  .tick-box--support { left: 353px; top: 229px; }

  .benefit {
    position: absolute; font-family: "Fira Sans", sans-serif; font-weight: 600;
    font-size: 23px; line-height: 26px; color: var(--label-dark);
  }
  .benefit--tests { left: 151px; top: 45px; }
  .benefit--recovery { left: 56px; top: 312px; }
  .benefit--support { left: 356px; top: 318px; }

  .megaphone-orbit { position: absolute; left: 95px; top: 65px; width: 264px; height: 264px; }
  .megaphone-art {
    position: absolute; left: 130px; top: 100px; width: 194px; height: 194px; border-radius: 50%;
    background: radial-gradient(circle at 40% 40%, #ffffff, #cfd6e2 70%, #aab4c6);
    box-shadow: 0 6px 16px rgba(0,0,0,.25);
  }

  .headline {
    position: absolute; left: 504px; top: 34px; width: 680px; text-align: center;
    font-family: "Anton", sans-serif; font-size: 40px; line-height: 48px; color: var(--heading-white);
    text-shadow: -2px -2px 0 var(--ink), 2px -2px 0 var(--ink), -2px 2px 0 var(--ink), 2px 2px 0 var(--ink), 0 3px 0 var(--ink);
  }
  .headline-stat {
    position: absolute; left: 560px; top: 108px; width: 600px; text-align: center;
    font-family: "Anton", sans-serif; font-size: 62px; line-height: 72px; color: var(--alert-red);
    text-shadow: -3px -3px 0 #fff, 3px -3px 0 #fff, -3px 3px 0 #fff, 3px 3px 0 #fff, 0 4px 6px rgba(0,0,0,.4);
  }
  .subheading {
    position: absolute; left: 580px; top: 212px; width: 580px; text-align: center;
    font-family: "Merienda", cursive; font-weight: 700; font-size: 25px; line-height: 40px; color: var(--sub-pink);
    text-shadow: 0 2px 3px rgba(0,0,0,.6);
  }
  .brand {
    position: absolute; left: 957px; top: 344px; width: 243px; height: 45px;
    background: var(--brand-red); display: flex; align-items: center; justify-content: center;
    font-family: "Fira Sans", sans-serif; font-weight: 700; font-size: 30px; color: #ffffff;
  }

  .delivery-band {
    position: absolute; left: 0; top: 393px; width: 1200px; height: 118px;
    background: linear-gradient(90deg, var(--band-dark), var(--band-violet) 55%, var(--band-dark));
    display: flex; flex-direction: column; align-items: center; justify-content: center;
    font-family: "Fira Sans", sans-serif; font-weight: 700; font-size: 37px; line-height: 46px; color: #ffffff;
  }
</style>
</head>
<body>
<div class="sheet">

  <section class="banner banner--top">
    <div class="tech-backdrop" role="img" aria-label="Glowing blue and red circuit board technology background"></div>
    <div class="light-panel"></div>
    <div class="diagonal-stripe"></div>
    <div class="banner-content">
      <svg class="megaphone-orbit" viewBox="0 0 264 264" aria-hidden="true">
        <circle cx="132" cy="132" r="124" fill="none" stroke="#c4cad4" stroke-width="10" stroke-dasharray="260 60"/>
      </svg>
      <div class="megaphone-art" role="img" aria-label="Red and blue megaphone illustration"></div>

      <div class="tick-box tick-box--tests"><svg viewBox="0 0 69 69"><path d="M14 36 L28 50 L56 18" fill="none" stroke="var(--tick-green)" stroke-width="8" stroke-linecap="round" stroke-linejoin="round"/></svg></div>
      <p class="benefit benefit--tests">Regular Backup<br>&amp; DR Tests</p>

      <div class="tick-box tick-box--recovery"><svg viewBox="0 0 69 69"><path d="M14 36 L28 50 L56 18" fill="none" stroke="var(--tick-green)" stroke-width="8" stroke-linecap="round" stroke-linejoin="round"/></svg></div>
      <p class="benefit benefit--recovery">Quick Recovery<br>Times</p>

      <div class="tick-box tick-box--support"><svg viewBox="0 0 69 69"><path d="M14 36 L28 50 L56 18" fill="none" stroke="var(--tick-green)" stroke-width="8" stroke-linecap="round" stroke-linejoin="round"/></svg></div>
      <p class="benefit benefit--support">24/7 Support</p>

      <h1 class="headline">RANSOMWARE HITS A BUSINESS</h1>
      <h2 class="headline-stat">EVERY 11 SECONDS</h2>
      <p class="subheading">Why take the risk of not being able to recover, let our Backup &amp; DR experts manage this for you</p>
      <div class="brand">Fennick</div>
    </div>
  </section>

  <div class="delivery-band">
    <p>Your email banner for marketing campaign is ready</p>
    <p>Size: 480×152</p>
  </div>

  <section class="banner banner--bottom">
    <div class="tech-backdrop" role="img" aria-label="Glowing blue and red circuit board technology background"></div>
    <div class="light-panel"></div>
    <div class="diagonal-stripe"></div>
    <div class="banner-content">
      <svg class="megaphone-orbit" viewBox="0 0 264 264" aria-hidden="true">
        <circle cx="132" cy="132" r="124" fill="none" stroke="#c4cad4" stroke-width="10" stroke-dasharray="260 60"/>
      </svg>
      <div class="megaphone-art" role="img" aria-label="Red and blue megaphone illustration"></div>

      <div class="tick-box tick-box--tests"><svg viewBox="0 0 69 69"><path d="M14 36 L28 50 L56 18" fill="none" stroke="var(--tick-green)" stroke-width="8" stroke-linecap="round" stroke-linejoin="round"/></svg></div>
      <p class="benefit benefit--tests">Regular Backup<br>&amp; DR Tests</p>

      <div class="tick-box tick-box--recovery"><svg viewBox="0 0 69 69"><path d="M14 36 L28 50 L56 18" fill="none" stroke="var(--tick-green)" stroke-width="8" stroke-linecap="round" stroke-linejoin="round"/></svg></div>
      <p class="benefit benefit--recovery">Quick Recovery<br>Times</p>

      <div class="tick-box tick-box--support"><svg viewBox="0 0 69 69"><path d="M14 36 L28 50 L56 18" fill="none" stroke="var(--tick-green)" stroke-width="8" stroke-linecap="round" stroke-linejoin="round"/></svg></div>
      <p class="benefit benefit--support">24/7 Support</p>

      <h1 class="headline">RANSOMWARE HITS A BUSINESS</h1>
      <h2 class="headline-stat">EVERY 11 SECONDS</h2>
      <p class="subheading">Why take the risk of not being able to recover, let our Backup &amp; DR experts manage this for you</p>
      <div class="brand">Fennick</div>
    </div>
  </section>

</div>
</body>
</html>
```